Website design for lighting products company

We want a design for our website. The website is for a company that sells lighting products. The structure is similar to the below website. We really like their design as well: www.ambervalelamps.com

Industry/Entity Type

Lighting

Number of Pages Required

5+ page

Colors

Designer to choose colors to be used in the design.

Requirements
Must have
• Simple design

```html
<!DOCTYPE html>
<html lang="en">
<head>
<meta charset="utf-8">
<title>Lighting Company</title>
<link href="https://fonts.googleapis.com/css2?family=Poppins:wght@300;400;500;600&display=swap" rel="stylesheet">
<style>
:root{
  --ink:#1d1d1d;
  --text:#555;
  --line:#e4e4e4;
  --panel:#f3f3f3;
  --accent:#f4c8b6;
  --accent-soft:#fcd6d3;
  --mint:#d4ebe6;
  --dark:#1b1b1b;
  --white:#fff;
  --footer:#f7f7f7;
  --copy:#e9e9e9;
}
*{box-sizing:border-box;margin:0;padding:0}
html,body{width:1200px;height:3000px;overflow:hidden}
body{font-family:'Poppins',sans-serif;color:var(--ink);background:var(--white);position:relative}
.abs{position:absolute}
.wrap{position:absolute;left:233px;width:734px}

/* top bar */
.topbar{top:0;left:0;width:1200px;height:28px;background:var(--footer);border-bottom:1px solid var(--line)}
.topbar nav{position:absolute;right:233px;top:0;height:28px;display:flex;align-items:center;gap:18px;font-size:8px;color:#666;text-transform:uppercase}
.topbar .phone{font-weight:600;font-size:11px;color:#444;display:flex;align-items:center;gap:5px}
.search-dot{width:16px;height:16px;border-radius:50%;background:var(--accent)}

/* header */
.header{top:28px;left:0;width:1200px;height:63px;border-bottom:1px solid var(--line)}
.brand{position:absolute;left:233px;top:22px;font-size:16px;font-weight:600;letter-spacing:.5px;display:flex;align-items:center;gap:7px;color:var(--ink)}
.brand i{width:9px;height:9px;background:var(--ink);display:inline-block}
.mainnav{position:absolute;right:235px;top:26px;display:flex;font-size:10px;text-transform:uppercase;color:#333}
.mainnav span{padding:0 14px;border-left:1px solid #ddd}
.mainnav span:first-child{border-left:none}

/* hero */
.hero{top:91px;left:0;width:1200px;height:516px;background:
  radial-gradient(ellipse 260px 120px at 900px 40px,rgba(255,255,255,.9),transparent 70%),
  linear-gradient(180deg,rgba(255,255,255,0) 70%,rgba(215,220,226,.8) 100%),
  linear-gradient(90deg,#f5f6f8 0%,#eef0f3 32%,#b7c3d3 52%,#7d93b3 64%,#c7a26a 72%,#9fb0c6 82%,#dde1e6 100%)}
.hero-copy{position:absolute;left:233px;top:202px}
.hero-copy .pre{font-size:15px;font-weight:300;color:#333}
.hero-copy .name{font-size:25px;font-weight:500;letter-spacing:.5px;color:var(--ink);margin-top:2px}
.hero-copy .sub{font-size:12px;color:#333;margin-top:14px}
.play{margin-top:25px;display:flex;align-items:center;height:43px}
.play .circle{width:43px;height:43px;border-radius:50%;background:var(--dark);display:flex;align-items:center;justify-content:center}
.play .label{background:var(--dark);color:#fff;font-size:12px;font-weight:600;height:36px;line-height:36px;padding:0 15px 0 8px;margin-left:-4px}
.arrow{position:absolute;top:240px;width:56px;height:56px;background:var(--dark);display:flex;align-items:center;justify-content:center}

/* brochures */
.brochures{top:653px;height:276px;background:var(--panel);border:1px solid var(--line)}
h2{font-size:19px;font-weight:600;letter-spacing:.2px;color:var(--ink)}
.rule{width:38px;height:3px;background:var(--accent);margin-top:9px}
.center{text-align:center}
.center .rule{margin:9px auto 0}
.broch-row{position:absolute;top:102px;left:26px;display:flex}
.broch{width:240px;display:flex;gap:12px;padding-right:20px}
.broch + .broch{padding-left:22px;border-left:1px solid var(--line)}
.broch .thumb{flex:none;width:78px;height:122px;background:linear-gradient(165deg,#3a3a3a 0%,#f4f4f4 22%,#e6e8ea 50%,#b9c0c6 62%,#7bbf3a 82%,#f6f6f6 100%);box-shadow:0 1px 3px rgba(0,0,0,.25)}
.broch .info{width:118px}
.broch h3{font-size:12px;font-weight:500;line-height:15px;color:var(--ink)}
.broch p{font-size:9.5px;line-height:15px;color:#555;margin-top:9px}
.link{display:inline-block;font-size:9.5px;font-weight:600;color:var(--ink);text-transform:uppercase;background:linear-gradient(transparent 60%,var(--accent) 60%);padding:0 4px}
.broch .link{margin-top:12px}
.pager{position:absolute;top:916px;left:565px;width:70px;height:26px;border-radius:13px;background:#e6e6e6;display:flex;align-items:center;justify-content:center;gap:4px}
.pager i{width:6px;height:6px;border-radius:50%;background:#bbb}
.pager i:first-child{background:#666}

/* welcome */
.welcome-copy{position:absolute;left:590px;top:1047px;width:376px}
.welcome-copy p{font-size:10.5px;line-height:16.3px;color:#555;text-align:justify;margin-top:25px}
.welcome-copy p + p{margin-top:16px}

/* gallery */
.tile{position:absolute;width:169px;height:156px}
.tile .cap{position:absolute;left:9px;top:9px;width:151px;height:138px;background:rgba(248,198,178,.92);display:flex;align-items:center;justify-content:center;font-size:15px;color:#222}

/* products */
.prod{position:absolute;width:170px}
.prod .box{width:170px;height:189px;border:1px solid var(--line);position:relative;background:#f5f5f5}
.prod .name{font-size:10px;font-weight:600;text-align:center;margin-top:20px;color:#222}
.prod .bar{position:absolute;left:0;bottom:0;width:100%;height:37px;background:var(--dark);color:#fff;font-size:9px;font-weight:600;display:flex;align-items:center;justify-content:center}

/* subscribe */
.subscribe{top:2494px;left:0;width:1200px;height:156px;background:var(--accent-soft)}
.subscribe h4{position:absolute;left:282px;top:67px;font-size:15px;font-weight:600}
.subscribe .field{position:absolute;left:577px;top:62px;width:231px;height:34px;background:#fff;font-size:9px;color:#999;padding-left:12px;line-height:34px}
.subscribe .btn{position:absolute;left:827px;top:62px;width:93px;height:34px;background:var(--dark);color:#fff;font-size:9px;font-weight:600;text-align:center;line-height:34px}

/* footer */
.footer{top:2650px;left:0;width:1200px;height:303px;background:var(--footer)}
.fcol{position:absolute;top:50px;font-size:9.5px;color:#555}
.fcol h5{font-size:8.5px;font-weight:600;color:#222;text-transform:uppercase;margin-bottom:14px}
.fcol ul{list-style:none;line-height:19px}
.fcol .pair{display:flex;gap:38px}
.contact-line{display:flex;gap:10px;margin-bottom:13px;line-height:13px}
.reviews{position:absolute;font-size:8.5px;color:#444}
.stars{color:#f0b44c;font-size:11px;letter-spacing:2px}
.social{display:flex;gap:6px;margin-top:12px}
.social i{width:26px;height:26px;border-radius:50%;border:1.5px solid #666}
.copyright{top:2953px;left:0;width:1200px;height:47px;background:var(--copy);text-align:center;font-size:9px;color:#555;line-height:47px}
</style>
</head>
<body>

<div class="abs topbar">
  <nav>
    <span>About</span><span>News</span><span>Careers</span><span>Contact</span>
    <span class="phone"><svg width="10" height="10" viewBox="0 0 24 24"><path d="M6.6 10.8a15 15 0 006.6 6.6l2.2-2.2c.3-.3.7-.4 1-.2 1.1.4 2.3.6 3.6.6.6 0 1 .4 1 1V20c0 .6-.4 1-1 1A17 17 0 013 4c0-.6.4-1 1-1h3.5c.6 0 1 .4 1 1 0 1.3.2 2.5.6 3.6.1.3 0 .7-.2 1z" fill="none" stroke="#777" stroke-width="1.8"/></svg>555-204-7718</span>
    <span class="search-dot"></span>
  </nav>
</div>

<header class="abs header">
  <div class="brand"><span>LIGHTING</span><i></i><span>COMPANY</span></div>
  <nav class="mainnav"><span>Products ›</span><span>Solutions ›</span><span>Case Studies</span><span>Downloads</span></nav>
</header>

<section class="abs hero" role="img" aria-label="Bright warehouse aisle with stocked shelves lit by ceiling fixtures">
  <div class="hero-copy">
    <div class="pre">WELCOME TO</div>
    <div class="name">LIGHTING COMPANY</div>
    <div class="sub">Largest Manufacturers of Commercial Lighting Solutions</div>
    <div class="play">
      <span class="circle"><svg width="14" height="16" viewBox="0 0 14 16"><path d="M2 1l11 7-11 7z" fill="#fff"/></svg></span>
      <span class="label">PLAY OUR FULL VIDEO</span>
    </div>
  </div>
  <div class="arrow" style="left:0"><svg width="14" height="22" viewBox="0 0 14 22"><path d="M12 2L3 11l9 9" stroke="#fff" stroke-width="2.5" fill="none"/></svg></div>
  <div class="arrow" style="right:0"><svg width="14" height="22" viewBox="0 0 14 22"><path d="M2 2l9 9-9 9" stroke="#fff" stroke-width="2.5" fill="none"/></svg></div>
</section>

<section class="wrap brochures">
  <div class="center" style="margin-top:34px"><h2>LATEST LIGHTING COMPANY BROCHURES</h2><div class="rule"></div></div>
  <div class="broch-row">
    <div class="broch"><div class="thumb" role="img" aria-label="Brochure cover showing a floodlight fixture"></div><div class="info"><h3>Pellentesque habitant morbi</h3><p>Phasellus lobortis dictum orci, nec rhoncus leo sodales vehicula.</p><span class="link">+ View Now</span></div></div>
    <div class="broch"><div class="thumb" role="img" aria-label="Brochure cover showing a floodlight fixture"></div><div class="info"><h3>Pellentesque habitant morbi</h3><p>Phasellus lobortis dictum orci, nec rhoncus leo sodales vehicula.</p><span class="link">+ View Now</span></div></div>
    <div class="broch"><div class="thumb" role="img" aria-label="Brochure cover showing a floodlight fixture"></div><div class="info"><h3>Pellentesque habitant morbi</h3><p>Phasellus lobortis dictum orci, nec rhoncus leo sodales vehicula.</p><span class="link">+ View Now</span></div></div>
  </div>
</section>
<div class="pager"><i></i><i></i><i></i><i></i></div>

<div class="abs" style="left:247px;top:1091px;width:237px;height:250px;background:var(--mint)"></div>
<div class="abs" role="img" aria-label="Blurred street market glowing with hanging lights at night" style="left:273px;top:1029px;width:263px;height:278px;background:
  radial-gradient(circle at 70% 22%,rgba(255,190,110,.85),transparent 30%),
  radial-gradient(circle at 25% 35%,rgba(240,150,70,.7),transparent 28%),
  radial-gradient(circle at 50% 60%,rgba(150,90,60,.6),transparent 40%),
  linear-gradient(180deg,#3a2418 0%,#2a1d18 55%,#3b3a40 100%)"></div>
<div class="welcome-copy">
  <h2>WELCOME TO LIGHTING COMPANY</h2><div class="rule"></div>
  <p>Lorem ipsum dolor sit amet, consectetur adipiscing elit. Vestibulum blandit lacinia tempor. Integer consequat pretium lobortis. Sed sem tortor, pharetra suscipit massa nec, placerat ultricies lacus. Fusce fringilla enim quam, vel porttitor turpis mattis eu. Nullam vitae eros ut diam viverra dictum. Donec sodales pretium tortor, eu ultricies tellus rutrum a. Vestibulum a libero sit amet arcu viverra mattis quis sit amet diam.</p>
  <p>Nullam vitae ex metus. Phasellus sed feugiat mi. Nullam id eleifend tellus. Interdum et malesuada fames ac ante ipsum primis in faucibus. Class aptent taciti sociosqu ad litora torquent per conubia nostra, per inceptos himenaeos.</p>
  <div style="margin-top:26px"><span class="link">+ Read More</span></div>
</div>

<div class="tile" style="left:234px;top:1425px;background:linear-gradient(180deg,#7a3a34 0%,#b98a80 45%,#d9b8ae 75%,#b3262b 100%)" role="img" aria-label="Classroom with ceiling lighting"><div class="cap">Education</div></div>
<div class="tile" style="left:422px;top:1425px;background:radial-gradient(ellipse 40px 90px at 50% 30%,#ffffff,transparent 70%),linear-gradient(180deg,#dcdcdc 0%,#eeeeee 45%,#cfd1d3 75%,#8e8e8e 100%)" role="img" aria-label="White office with linear ceiling lights and chairs"></div>
<div class="tile" style="left:609px;top:1425px;background:linear-gradient(180deg,#e2563f 0%,#c74a3a 18%,#3d3d40 30%,#6d7177 50%,#c5c7c9 72%,#f1f1f1 100%)" role="img" aria-label="Long office corridor with red ceiling and glass walls"></div>
<div class="tile" style="left:797px;top:1425px;background:radial-gradient(ellipse 70px 40px at 75% 75%,#c9a57c,transparent 70%),linear-gradient(180deg,#eef0f1 0%,#b9bec2 35%,#6c7278 65%,#5b6a4a 100%)" role="img" aria-label="Bright lounge with bean bags and wooden tables"></div>
<div class="tile" style="left:234px;top:1600px;background:linear-gradient(180deg,#1f5fb8 0%,#4f8fd6 30%,#cfe3f5 55%,#6fa3dc 75%,#d9e7f4 100%)" role="img" aria-label="Blue-lit glass hallway"></div>
<div class="tile" style="left:422px;top:1600px;background:radial-gradient(circle at 50% 30%,#e8b44f 0%,#b88432 22%,transparent 40%),linear-gradient(180deg,#f3efe8 0%,#e6ddd0 50%,#243036 72%,#7b2a1f 100%)" role="img" aria-label="Room with golden chandelier"></div>
<div class="tile" style="left:609px;top:1600px;background:radial-gradient(ellipse 60px 30px at 50% 28%,#fff7d8,transparent 75%),linear-gradient(180deg,#e7e4de 0%,#f6f2e6 40%,#a8988a 70%,#3c3a38 100%)" role="img" aria-label="Ring pendant lights above a living room"></div>
<div class="tile" style="left:797px;top:1600px;background:radial-gradient(circle at 55% 15%,#e7dbb0,transparent 25%),radial-gradient(circle at 40% 85%,#c2463a,transparent 20%),linear-gradient(180deg,#5e5848 0%,#3a372f 55%,#1d1c19 100%)" role="img" aria-label="Street lamps on a foggy road at night"></div>

<div class="abs center" style="left:0;width:1200px;top:1820px"><h2>AN EXTENSIVE PRODUCT RANGE</h2><div class="rule"></div></div>

<div class="prod" style="left:233px;top:1901px"><div class="box" role="img" aria-label="Skyline Duo linear fitting" style="background:linear-gradient(135deg,#fafafa 20%,#d9dadb 45%,#f6f6f6 55%,#efefef 100%)"><div class="bar">+ VIEW NOW</div></div><div class="name">Skyline Duo</div></div>
<div class="prod" style="left:421px;top:1901px"><div class="box" role="img" aria-label="Harbor Line Surface fitting" style="background:linear-gradient(150deg,#f7f7f7 10%,#6a6b6d 30%,#a9aaac 42%,#f4f4f4 60%,#eeeeee 100%)"></div><div class="name">Harbor Line Surface</div></div>
<div class="prod" style="left:608px;top:1901px"><div class="box" role="img" aria-label="Harbor Line Suspended fitting" style="background:linear-gradient(90deg,#f4f4f4 30%,#bfc0c2 42%,#e9e9e9 50%,#bfc0c2 58%,#f4f4f4 70%)"></div><div class="name">Harbor Line Suspended</div></div>
<div class="prod" style="left:796px;top:1901px"><div class="box" role="img" aria-label="Harbor Line Recessed fitting" style="background:linear-gradient(150deg,#f6f6f6 25%,#dcdcdc 45%,#fbfbfb 55%,#f0f0f0 100%)"></div><div class="name">Harbor Line Recessed</div></div>
<div class="prod" style="left:233px;top:2149px"><div class="box" role="img" aria-label="Meridian Suspended fitting" style="background:linear-gradient(145deg,#f6f6f6 25%,#cfd0d2 42%,#fafafa 55%,#efefef 100%)"></div><div class="name">Meridian Suspended</div></div>
<div class="prod" style="left:421px;top:2149px"><div class="box" role="img" aria-label="Softbay ceiling panel" style="background:radial-gradient(ellipse 60px 25px at 50% 50%,#ffffff,#e3e4e5 70%,transparent 72%),linear-gradient(180deg,#f7f7f7,#eeeeee)"></div><div class="name">Softbay</div></div>
<div class="prod" style="left:608px;top:2149px"><div class="box" role="img" aria-label="Metrobeam linear fitting" style="background:linear-gradient(145deg,#f6f6f6 25%,#c9cacc 42%,#fdfdfd 52%,#efefef 100%)"></div><div class="name">Metrobeam</div></div>
<div class="prod" style="left:796px;top:2149px"><div class="box" role="img" aria-label="Round white downlight unit" style="background:radial-gradient(circle at 50% 48%,#ffffff 0%,#d7d8da 28%,#f0f0f0 34%,transparent 36%),linear-gradient(180deg,#f7f7f7,#eeeeee)"></div><div class="name">Air Control System Overview</div></div>

<div class="abs center" style="left:0;width:1200px;top:2421px"><span class="link">+ View All Products</span></div>

<section class="abs subscribe">
  <h4>Subscribe to News and Updates</h4>
  <div class="field">Enter your email address</div>
  <div class="btn">SUBSCRIBE</div>
</section>

<footer class="abs footer">
  <div class="fcol" style="left:234px">
    <h5>Contact Info</h5>
    <div class="contact-line"><svg width="11" height="14" viewBox="0 0 12 16"><path d="M6 0a6 6 0 00-6 6c0 4.5 6 10 6 10s6-5.5 6-10a6 6 0 00-6-6zm0 8.5A2.5 2.5 0 116 3.5a2.5 2.5 0 010 5z" fill="#222"/></svg><span>4715 Street Name,<br>City, Country - Y123</span></div>
    <div class="contact-line"><svg width="11" height="11" viewBox="0 0 24 24"><path d="M6.6 10.8a15 15 0 006.6 6.6l2.2-2.2c.3-.3.7-.4 1-.2 1.1.4 2.3.6 3.6.6.6 0 1 .4 1 1V20c0 .6-.4 1-1 1A17 17 0 013 4c0-.6.4-1 1-1h3.5c.6 0 1 .4 1 1 0 1.3.2 2.5.6 3.6.1.3 0 .7-.2 1z" fill="#222"/></svg><span>000-123-4567</span></div>
    <div class="contact-line"><svg width="12" height="10" viewBox="0 0 24 18"><path d="M0 0h24v18H0z" fill="#222"/><path d="M0 0l12 9 12-9" stroke="#f7f7f7" stroke-width="2" fill="none"/></svg><span>info@companyname.com</span></div>
  </div>
  <div class="fcol" style="left:429px">
    <h5>Quick Links</h5>
    <div class="pair"><ul><li>Products</li><li>Solutions</li><li>Case Studies</li><li>Downloads</li></ul><ul><li>About Us</li><li>Blog</li><li>FAQ</li><li>Contact Us</li></ul></div>
  </div>
  <div class="fcol" style="left:635px">
    <h5>Information</h5>
    <ul><li>Search Terms</li><li>Advanced Search</li><li>Help &amp; Faq's</li><li>Careers</li></ul>
  </div>
  <div class="fcol" style="left:790px">
    <h5>Useful Links</h5>
    <ul><li>Privacy Policy</li><li>Returns</li><li>Terms &amp; Conditions</li><li>Sitemap</li></ul>
  </div>
  <div class="reviews" style="left:242px;top:206px;font-weight:600">LIGHTING COMPANY REVIEWS</div>
  <div class="reviews" style="left:386px;top:202px">OVERALL RATING / 16 TOTAL 1ST-PARTY REVIEWS<br><span class="stars">★★★★★</span> <span style="font-size:12px">5.0</span> OUT OF 5 STARS &nbsp;&nbsp;<u>VIEW REVIEWS</u></div>
  <div class="reviews" style="left:665px;top:204px">
    <div style="font-weight:600">FOLLOW US ON SOCIAL MEDIA</div>
    <div class="social"><i></i><i></i><i></i><i></i><i></i></div>
  </div>
</footer>

<div class="abs copyright">Copyright © 2019 Lighting. All Rights Reserved</div>

</body>
</html>
```